Plakat-Design für Fahrschule
Zielgruppe
Zielgruppe Fahrschüler, Thema: Theorie Lern Plan
Aufgabenstellung
A3 Querformat, Wir benötigen für den Theorielernplan ein Plakat, mit Tabellen und Texten (siehe PDF), der Stil darf gerne Kreativ sein, aber nicht zu verspielt, keine klassischen Fahrschulsymbole wie Lenkräder, Autos usw.
Farben: weiß, schwarz, petrol und je nach Bedarf

```html
<!DOCTYPE html>
<html lang="de">
<head>
<meta charset="utf-8">
<title>Mein Prüfungstag – Theorie-Lernplan</title>
<link href="https://fonts.googleapis.com/css2?family=Montserrat:wght@700;800&family=Oswald:wght@300;400;600&display=swap" rel="stylesheet">
<style>
  :root{
    --petrol:#006570;
    --paper:#efefef;
    --ink:#111111;
    --white:#ffffff;
    --soft-grey:#dcdcdc;
  }
  *{margin:0;padding:0;box-sizing:border-box}
  html,body{width:1200px;height:801px;overflow:hidden;background:var(--paper)}
  .poster{position:relative;width:1200px;height:801px;background:var(--paper);color:var(--ink);font-family:'Oswald',sans-serif}
  .shapes{position:absolute;left:0;top:0}
  .title{position:absolute;left:0;width:1200px;top:22px;text-align:center;font-family:'Montserrat',sans-serif;font-weight:800;font-size:31px;color:var(--petrol);letter-spacing:.5px}

  .step-head{position:absolute;text-align:right;font-family:'Montserrat',sans-serif;font-weight:800;line-height:1;padding-left:6px;background:var(--paper)}
  .step-head .num{font-size:27px;display:block}
  .step-head .label{font-size:17px;display:block;margin-top:2px}
  .step-head.on-petrol{background:var(--petrol);color:var(--white)}
  .step-text{position:absolute;font-weight:300;font-size:10.5px;line-height:15.5px;letter-spacing:-.1px;color:var(--ink)}
  .step-text.on-petrol{color:var(--white)}
  .step-text strong{font-weight:600}

  .figure{position:absolute;left:720px;top:180px;width:160px;height:232px;background:linear-gradient(180deg,rgba(0,101,112,.18),rgba(0,101,112,.35));border-radius:6px}

  .plan{position:absolute;left:0;top:413px;width:1200px;height:311px;background:var(--petrol);color:var(--white)}
  .week{position:absolute;top:16px}
  .week-title{font-family:'Montserrat',sans-serif;font-weight:800;font-size:26px;line-height:1}
  .week-title small{font-size:18px;text-transform:uppercase;margin-left:4px}
  .week-table{display:grid;grid-template-columns:48px 140px 150px;margin-top:10px}
  .week-table .th{font-weight:600;font-size:16px;height:32px}
  .week-table .day{font-weight:600;font-size:15px;height:30.5px;line-height:30.5px}
  .week-table .count{font-weight:300;font-size:11px;height:30.5px;line-height:30.5px;padding-left:46px}
  .week-table .passed{height:30.5px;display:flex;align-items:center;gap:4px}
  .ring{width:19px;height:19px;border:2.5px solid var(--white);border-radius:50%}
  .week-note{position:absolute;left:290px;top:66px;height:186px;writing-mode:vertical-rl;transform:rotate(180deg);font-weight:300;font-size:10px;line-height:13px}

  .footer{position:absolute;left:0;top:724px;width:1200px;height:77px}
  .exam-day{position:absolute;left:31px;top:22px;display:flex;align-items:center;gap:12px}
  .exam-day .big{font-family:'Montserrat',sans-serif;font-weight:800;font-size:25px}
  .exam-day .big small{font-size:18px}
  .exam-day .goal{font-weight:600;font-size:17px;margin-left:4px}
  .motto{position:absolute;left:759px;top:40px;width:230px;white-space:nowrap;font-weight:400;font-size:10.5px;color:var(--petrol)}
  .brand{position:absolute;left:1010px;top:20px;width:175px;height:42px;border:2px solid var(--ink);text-align:center;white-space:nowrap;overflow:hidden;font-family:'Montserrat',sans-serif;font-weight:700;font-size:13px;line-height:38px;letter-spacing:.3px}
</style>
</head>
<body>
<main class="poster">
  <svg class="shapes" width="1200" height="801" viewBox="0 0 1200 801">
    <g fill="none" stroke="var(--ink)" stroke-width="2.2">
      <circle cx="80" cy="87" r="16"/>
      <circle cx="929" cy="41" r="9"/>
      <circle cx="423" cy="278" r="9"/>
      <circle cx="174" cy="353" r="9"/>
      <circle cx="1107" cy="369" r="16"/>
      <path d="M18 268h60M35 277h68M30 277h3"/>
      <path d="M760 90h68M748 98h65M820 98h3"/>
      <path d="M462 331h72M450 339h55M512 339h3"/>
      <path d="M156 86h206a20 20 0 0 1 20 20v195a20 20 0 0 1-20 20h-67l-36 59-38-59h-65a20 20 0 0 1-20-20v-195a20 20 0 0 1 20-20z"/>
      <path d="M495 86h208a20 20 0 0 1 20 20v195a20 20 0 0 1-20 20h-66l-39 59-39-59h-64a20 20 0 0 1-20-20v-195a20 20 0 0 1 20-20z"/>
      <path d="M153 108h53v46a12 12 0 0 1-12 12h-29a12 12 0 0 1-12-12z M165 117h30"/>
      <path d="M496 108h40M496 166h40M502 108c0 20 26 20 26 29s-26 9-26 29M530 108c0 20-26 20-26 29s26 9 26 29"/>
      <path d="M368 194h2M375 194h52M420 187l7 7-7 7"/>
      <path d="M711 196h2M718 196h52M763 189l7 7-7 7"/>
      <path d="M926 355v3M926 362v46M919 401l7 7 7-7"/>
    </g>
    <circle cx="395" cy="334" r="50" fill="var(--soft-grey)" opacity=".7"/>
    <path d="M922 86h206a20 20 0 0 1 20 20v195a20 20 0 0 1-20 20h-63l-40 59-35-59h-68a20 20 0 0 1-20-20v-195a20 20 0 0 1 20-20z" fill="var(--petrol)"/>
    <g fill="none" stroke="var(--white)" stroke-width="2.2">
      <path d="M932 108h46v14c0 14-10 24-23 24s-23-10-23-24z M932 114h-8c0 14 6 20 14 22M978 114h8c0 14-6 20-14 22M955 146v12M943 166l12-8 12 8z"/>
    </g>
  </svg>

  <h1 class="title">MEIN PRÜFUNGSTAG</h1>

  <div class="step-head" style="right:810px;top:136px"><span class="num">01</span><span class="label">ANMELDUNG</span></div>
  <p class="step-text" style="left:153px;top:262px;width:215px">Nachdem du dich bei der Fahrschule angemeldet hast, machst du in deiner Theorie-App alle Fragen einmal durch.</p>

  <div class="step-head" style="right:470px;top:137px"><span class="num">02</span><span class="label">VORPRÜFUNG</span></div>
  <p class="step-text" style="left:495px;top:231px;width:215px">Du hast bereits jede Frage einmal beantwortet. Nun machst du 4 Vorprüfungen hintereinander. Hast du 3 von 4 Vorprüfungen bestanden, kannst du mit Schritt 3 weitermachen. Sollte das nicht klappen, wiederhole dies am nächsten Tag.</p>

  <div class="step-head on-petrol" style="right:141px;top:137px"><span class="num">03</span><span class="label">PRÜFUNG</span></div>
  <p class="step-text on-petrol" style="left:924px;top:202px;width:215px"><strong>Schritt 3 startet sobald du deinen Theorie-Prüfungstermin hast. Endphase 3 Wochen vor Prüfung.</strong></p>
  <p class="step-text on-petrol" style="left:924px;top:264px;width:215px">Folge den unten aufgeführten Plan. Du kannst natürlich auch täglich mehr lernen als aufgeführt. Zu viel gelernt hat noch niemand.</p>

  <div class="figure" role="img" aria-label="Illustration: Fahrschülerin springt über eine gestreifte Hürde"></div>

  <section class="plan">
    <div class="week" style="left:34px">
      <div class="week-title">01. <small>Woche</small></div>
      <div class="week-table">
        <div class="th">Tag</div><div class="th">Vorprüfungen</div><div class="th">Bestanden</div>
        <div class="day">01</div><div class="count">3</div><div class="passed"><i class="ring"></i><i class="ring"></i><i class="ring"></i></div>
        <div class="day">02</div><div class="count">3</div><div class="passed"><i class="ring"></i><i class="ring"></i><i class="ring"></i></div>
        <div class="day">03</div><div class="count">3</div><div class="passed"><i class="ring"></i><i class="ring"></i><i class="ring"></i></div>
        <div class="day">04</div><div class="count">3</div><div class="passed"><i class="ring"></i><i class="ring"></i><i class="ring"></i></div>
        <div class="day">05</div><div class="count">3</div><div class="passed"><i class="ring"></i><i class="ring"></i><i class="ring"></i></div>
        <div class="day">06</div><div class="count">3</div><div class="passed"><i class="ring"></i><i class="ring"></i><i class="ring"></i></div>
        <div class="day">07</div><div class="count" style="padding-left:36px">Pause</div><div></div>
      </div>
      <p class="week-note">Hast du weniger als 12 bestandene Vorprüfungen, mache an Tag 7 keine Pause, sondern weitere Vorprüfungen.</p>
    </div>

    <div class="week" style="left:438px">
      <div class="week-title">02. <small>Woche</small></div>
      <div class="week-table">
        <div class="th">Tag</div><div class="th">Vorprüfungen</div><div class="th">Bestanden</div>
        <div class="day">08</div><div class="count">4</div><div class="passed"><i class="ring"></i><i class="ring"></i><i class="ring"></i><i class="ring"></i></div>
        <div class="day">09</div><div class="count">4</div><div class="passed"><i class="ring"></i><i class="ring"></i><i class="ring"></i><i class="ring"></i></div>
        <div class="day">10</div><div class="count">4</div><div class="passed"><i class="ring"></i><i class="ring"></i><i class="ring"></i><i class="ring"></i></div>
        <div class="day">11</div><div class="count">4</div><div class="passed"><i class="ring"></i><i class="ring"></i><i class="ring"></i><i class="ring"></i></div>
        <div class="day">12</div><div class="count">4</div><div class="passed"><i class="ring"></i><i class="ring"></i><i class="ring"></i><i class="ring"></i></div>
        <div class="day">13</div><div class="count">4</div><div class="passed"><i class="ring"></i><i class="ring"></i><i class="ring"></i><i class="ring"></i></div>
        <div class="day">14</div><div class="count" style="padding-left:36px">Pause</div><div></div>
      </div>
      <p class="week-note" style="left:298px">Hast du weniger als 20 bestandene Vorprüfungen, mache an Tag 14 keine Pause, sondern weitere Vorprüfungen.</p>
    </div>

    <div class="week" style="left:858px">
      <div class="week-title">03. <small>Woche</small></div>
      <div class="week-table" style="grid-template-columns:48px 140px 170px">
        <div class="th">Tag</div><div class="th">Vorprüfungen</div><div class="th">Bestanden</div>
        <div class="day">15</div><div class="count">5</div><div class="passed"><i class="ring"></i><i class="ring"></i><i class="ring"></i><i class="ring"></i><i class="ring"></i></div>
        <div class="day">16</div><div class="count">5</div><div class="passed"><i class="ring"></i><i class="ring"></i><i class="ring"></i><i class="ring"></i><i class="ring"></i></div>
        <div class="day">17</div><div class="count">5</div><div class="passed"><i class="ring"></i><i class="ring"></i><i class="ring"></i><i class="ring"></i><i class="ring"></i></div>
        <div class="day">18</div><div class="count">5</div><div class="passed"><i class="ring"></i><i class="ring"></i><i class="ring"></i><i class="ring"></i><i class="ring"></i></div>
        <div class="day">19</div><div class="count">6</div><div class="passed"><i class="ring"></i><i class="ring"></i><i class="ring"></i><i class="ring"></i><i class="ring"></i><i class="ring"></i></div>
        <div class="day">20</div><div class="count">6</div><div class="passed"><i class="ring"></i><i class="ring"></i><i class="ring"></i><i class="ring"></i><i class="ring"></i><i class="ring"></i></div>
        <div class="day">21</div><div class="count">6</div><div class="passed"><i class="ring"></i><i class="ring"></i><i class="ring"></i><i class="ring"></i><i class="ring"></i><i class="ring"></i></div>
      </div>
    </div>
  </section>

  <footer class="footer">
    <div class="exam-day">
      <span class="big">22. <small>Tag</small></span>
      <svg width="62" height="14" viewBox="0 0 62 14" fill="none" stroke="var(--ink)" stroke-width="2.2"><path d="M0 7h3M9 7h51M53 1l7 6-7 6"/></svg>
      <span class="goal">Dein Prüfungstag</span>
      <svg width="74" height="50" viewBox="0 0 74 50" fill="none" stroke="var(--ink)" stroke-width="2.2" style="margin-left:22px;margin-top:-8px"><path d="M2 16 36 4l34 12-34 12z M16 21v12c0 6 10 9 20 9s20-3 20-9V21 M62 19v18 M59 37h6v9h-6z"/></svg>
    </div>
    <p class="motto">Denk immer daran, zu viel gelernt hat noch niemand!</p>
    <div class="brand">FAHRKLAR AKADEMIE</div>
  </footer>
</main>
</body>
</html>
```